Ledgerwise Business Card Design

Business Card Design for new business called Ledgerwise focused on selling business software to small and medium size companies who have outgrown Tallymark. Similar companies would be Tallymark, Nuvo, CoreFlow. Also Dealharbor would be good to look at for additional ideas around look and feel.

Target Market(s)

Business to Business

Industry/Entity Type

Information Technology

Contact Information for Business Card

Standard Business Card Information

Font styles to use
Sans Serif

```html
<!DOCTYPE html>
<html lang="en">
<head>
<meta charset="UTF-8">
<title>Ledgerwise Business Card</title>
<link rel="stylesheet" href="https://fonts.googleapis.com/css2?family=Open+Sans:wght@400;600;700&display=swap">
<style>
  :root {
    --navy: #0c4676;
    --band: #104e80;
    --band-deep: #0b3f6a;
    --orange: #f08a24;
    --white: #ffffff;
    --paper: #fbfbfb;
    --backdrop: #e7e4df;
    --ink-light: #e8eef5;
  }
  * { margin: 0; padding: 0; box-sizing: border-box; }
  html, body {
    width: 1200px; height: 950px; overflow: hidden;
    background: var(--backdrop);
    font-family: "Open Sans", Arial, sans-serif;
  }
  .sheet {
    position: relative; width: 1200px; height: 950px;
  }
  .card {
    position: absolute; left: 250px; width: 700px; height: 400px;
    border-radius: 6px; overflow: hidden;
    box-shadow: 0 10px 28px rgba(0,0,0,0.18);
  }
  .card-front { top: 40px; background: var(--paper); }
  .card-back {
    top: 490px;
    background: linear-gradient(135deg, var(--band) 0%, var(--band-deep) 100%);
  }

  /* Front */
  .brand-area {
    position: absolute; left: 0; top: 0; width: 100%; height: 178px;
    display: flex; align-items: center; justify-content: center;
    gap: 16px;
  }
  .brand-name {
    font-weight: 700; font-size: 50px; color: var(--navy);
    letter-spacing: -0.5px;
  }
  .brand-dot {
    width: 46px; height: 46px; border-radius: 50%; background: var(--orange);
  }
  .info-band {
    position: absolute; left: 0; top: 178px; width: 100%; height: 222px;
    background: linear-gradient(135deg, var(--band) 0%, var(--band-deep) 100%);
  }
  .person {
    position: absolute; left: 36px; top: 26px; color: var(--ink-light);
    font-size: 17px; line-height: 25px;
  }
  .person-name {
    color: var(--orange); font-weight: 600; font-size: 21px; margin-bottom: 2px;
  }
  .contacts {
    position: absolute; right: 32px; bottom: 28px; list-style: none;
    color: var(--ink-light); font-size: 17px; line-height: 30px; text-align: right;
  }
  .contacts li { display: flex; align-items: center; justify-content: flex-end; gap: 10px; }
  .contacts svg { width: 18px; height: 18px; fill: var(--orange); flex: none; }

  /* Back */
  .back-mark {
    position: absolute; left: 50%; top: 110px; width: 150px; height: 150px;
    margin-left: -75px; border-radius: 50%; background: var(--orange);
  }
  .back-web {
    position: absolute; left: 0; width: 100%; top: 296px; text-align: center;
    color: var(--ink-light); font-size: 18px;
  }
</style>
</head>
<body>
<main class="sheet">
  <section class="card card-front" aria-label="Business card front">
    <div class="brand-area">
      <span class="brand-name">Ledgerwise</span>
      <span class="brand-dot" aria-hidden="true"></span>
    </div>
    <div class="info-band">
      <div class="person">
        <p class="person-name">Mara Ellison</p>
        <p>President</p>
        <p>2190 Linden Crest Road</p>
        <p>Harlow Bay, NJ 07740</p>
      </div>
      <ul class="contacts">
        <li>555 0142 7781
          <svg viewBox="0 0 24 24" aria-hidden="true"><path d="M6.6 10.8a15.1 15.1 0 0 0 6.6 6.6l2.2-2.2a1 1 0 0 1 1-.25 11.4 11.4 0 0 0 3.6.57 1 1 0 0 1 1 1V20a1 1 0 0 1-1 1A17 17 0 0 1 3 4a1 1 0 0 1 1-1h3.5a1 1 0 0 1 1 1c0 1.25.2 2.45.57 3.57a1 1 0 0 1-.25 1z"/></svg>
        </li>
        <li>555 0196 3304
          <svg viewBox="0 0 24 24" aria-hidden="true"><path d="M7 3h8l3 3v4H7z M4 10h16a1 1 0 0 1 1 1v8a1 1 0 0 1-1 1H4a1 1 0 0 1-1-1v-8a1 1 0 0 1 1-1z M7 13h4v2H7z"/></svg>
        </li>
        <li>mara@ledgerwise.co
          <svg viewBox="0 0 24 24" aria-hidden="true"><path d="M3 5h18a1 1 0 0 1 1 1v12a1 1 0 0 1-1 1H3a1 1 0 0 1-1-1V6a1 1 0 0 1 1-1zm1 2.3V17h16V7.3l-8 5.2z M4.5 7l7.5 4.8L19.5 7z"/></svg>
        </li>
        <li>www.ledgerwise.co
          <svg viewBox="0 0 24 24" aria-hidden="true"><path d="M12 2a10 10 0 1 0 0 20 10 10 0 0 0 0-20zm6.9 6h-3a15 15 0 0 0-1.3-3.8A8 8 0 0 1 18.9 8zM12 4c.8 1.1 1.5 2.5 1.9 4h-3.8c.4-1.5 1.1-2.9 1.9-4zM4.3 14a8 8 0 0 1 0-4h3.4a16 16 0 0 0 0 4zm.8 2h3a15 15 0 0 0 1.3 3.8A8 8 0 0 1 5.1 16zm3-8h-3a8 8 0 0 1 4.3-3.8A15 15 0 0 0 8.1 8zM12 20c-.8-1.1-1.5-2.5-1.9-4h3.8c-.4 1.5-1.1 2.9-1.9 4zm2.3-6H9.7a14 14 0 0 1 0-4h4.6a14 14 0 0 1 0 4zm.3 5.8A15 15 0 0 0 15.9 16h3a8 8 0 0 1-4.3 3.8zM16.3 14a16 16 0 0 0 0-4h3.4a8 8 0 0 1 0 4z"/></svg>
        </li>
      </ul>
    </div>
  </section>

  <section class="card card-back" aria-label="Business card back">
    <div class="back-mark" aria-hidden="true"></div>
    <p class="back-web">www.ledgerwise.co</p>
  </section>
</main>
</body>
</html>
```